Free word Download template and Blog Design template

Looking for a free dowload template and blog template that we can use over and again. To see our current look, check out our website at www.velmarcrest.com.au. Further, other design docs attached. We would like to make this one a little less formal, although using similar branding.
Updates

Please note this design will be used as a template for content that can be dowloaded by a user.

Industry/Entity Type

Consulting

Requirements
Must have
• My project must be a word template

```html
<!DOCTYPE html>
<html lang="en">
<head>
<meta charset="utf-8">
<title>Velmar Crest – Company Proposal Word Template</title>
<link rel="stylesheet" href="https://fonts.googleapis.com/css2?family=Montserrat:wght@400;500;600;700;800&display=swap">
<style>
  :root{
    --board:#4d4d4d;
    --navy:#13296a;
    --navy-deep:#0b1a4a;
    --gold:#bba873;
    --gold-soft:#cdbd8f;
    --ink:#1b1b1b;
    --rule:#b7b7b7;
    --white:#ffffff;
  }
  *{box-sizing:border-box;margin:0;padding:0}
  html,body{width:1200px;height:2412px;overflow:hidden;background:var(--board)}
  body{font-family:"Montserrat",sans-serif;color:var(--ink)}
  .board{position:absolute;left:0;top:0;width:1281px;height:2576px;transform:scale(0.936768);transform-origin:0 0;background:var(--board)}

  .board-brand{position:absolute;left:0;right:0;top:118px;text-align:center;color:var(--white);font-weight:400;font-size:66px;letter-spacing:3px;line-height:1}

  .page{position:absolute;width:471px;height:666px;background:var(--white);overflow:hidden;box-shadow:0 5px 7px rgba(0,0,0,.35)}
  .col-left{left:143px}.col-right{left:662px}
  .row-1{top:274px}.row-2{top:991px}.row-3{top:1708px}

  .frame{position:absolute;left:0;top:0;width:471px;height:666px}
  .footer-text{position:absolute;top:646px;font-size:8.2px;font-weight:700;color:var(--white);letter-spacing:.1px;white-space:nowrap}
  .footer-text--left{left:25px}
  .footer-text--right{right:25px}
  .footer-text .year{color:var(--gold)}

  .page-title{position:absolute;left:28px;top:41px;font-weight:800;line-height:1}
  .page-title .line-1{display:block;font-size:17px;color:var(--navy)}
  .page-title .line-2{display:block;font-size:22px;color:var(--gold);margin-top:1px}
  .brand-mini{position:absolute;right:27px;top:47px;font-size:11.5px;font-weight:500;color:var(--navy);letter-spacing:.2px;white-space:nowrap}

  .content{position:absolute;left:26px;right:24px}
  .body-copy{font-size:6.35px;line-height:11.6px;text-align:justify;color:var(--ink)}
  .h-gold{font-size:14.5px;font-weight:600;color:var(--gold);line-height:1;margin-bottom:5px}
  .h-dark{font-size:11px;font-weight:600;color:var(--ink);line-height:1;margin-bottom:4px}
  .h-section{font-size:15px;font-weight:600;color:var(--ink);line-height:1;margin-bottom:5px}
  .quote{font-size:15px;font-weight:600;color:var(--gold);line-height:1;margin-bottom:4px}

  /* cover */
  .cover-photo{position:absolute;left:0;top:0;width:471px;height:508px;background:linear-gradient(160deg,#0a0f1c 0%,#111b30 35%,#1d3a5c 60%,#0e1a2c 100%)}
  .cover-art{position:absolute;left:0;top:0}
  .cover-brand{position:absolute;left:74px;top:50px;font-size:27px;font-weight:400;color:var(--white);letter-spacing:.5px;white-space:nowrap}
  .cover-heading{position:absolute;left:76px;top:122px;font-weight:800;font-size:41px;line-height:44px;color:var(--white);white-space:nowrap}
  .cover-heading .accent{color:var(--gold)}
  .cover-tagline{position:absolute;left:75px;top:258px;font-size:10.2px;line-height:10px;color:var(--white);font-weight:500;white-space:nowrap}
  .cover-doc{position:absolute;right:16px;top:540px;text-align:right;font-weight:800;font-size:28px;line-height:28.5px}
  .cover-doc .navy{color:var(--navy)}
  .cover-doc .gold{color:var(--gold)}
  .cover-web{position:absolute;right:15px;top:632px;font-size:9.6px;font-weight:500;letter-spacing:1.4px;color:var(--ink);white-space:nowrap}

  /* contents */
  .toc{position:absolute;left:42px;right:42px;top:131px}
  .toc-group{margin-bottom:33px}
  .toc-row{display:flex;align-items:baseline;font-size:8.4px;line-height:14px;color:var(--navy);font-weight:500}
  .toc-row--title{color:var(--gold);font-weight:700}
  .toc-row .label{white-space:nowrap;width:112px}
  .toc-row .leader{flex:1;border-bottom:1px dotted #9a9a9a;margin:0 4px 0 2px;transform:translateY(-2px)}
  .toc-row .num{width:6px;text-align:right;color:var(--ink)}
  .toc-rail{position:absolute;left:32px;top:134px}

  /* table */
  .data-table{position:absolute;left:24px;top:455px;width:424px;height:110px}
  .data-table .cell{position:absolute;font-size:5.6px;line-height:7px;color:var(--ink);white-space:nowrap}
  .data-table .head{color:var(--white);text-align:center;line-height:7px}

  /* chart */
  .chart{position:absolute;left:240px;top:352px}
  .list{font-size:6.4px;line-height:13px;color:var(--ink);padding-left:30px;margin-bottom:12px;white-space:nowrap}
  .sub-h{font-size:10.5px;font-weight:600;color:var(--ink);line-height:1;margin-bottom:9px;white-space:nowrap}

  /* two columns */
  .col{position:absolute;width:189px}
  .photo{width:189px;height:128px;background:linear-gradient(120deg,#c9ccd3 0%,#e7e3dc 45%,#9aa1ad 100%);border:1px solid var(--gold);margin:9px 0 8px}
</style>
</head>
<body>
<div class="board">

  <div class="board-brand">VELMAR CREST</div>

  <!-- Cover -->
  <section class="page col-left row-1 cover">
    <div class="cover-photo" role="img" aria-label="Photo of glass office towers seen from below at dusk"></div>
    <svg class="cover-art" width="471" height="666" viewBox="0 0 471 666">
      <defs>
        <linearGradient id="navyWedge" x1="0" y1="0" x2="1" y2="1">
          <stop offset="0" stop-color="#0b1a4a" stop-opacity=".75"/>
          <stop offset=".5" stop-color="#13296a"/>
          <stop offset="1" stop-color="#0f2360"/>
        </linearGradient>
      </defs>
      <polygon points="0,190 140,508 147,538 194,666 0,666" fill="url(#navyWedge)"/>
      <polygon points="233,508 471,508 471,666 194,666 147,538 218,538" fill="#ffffff"/>
      <polygon points="135,508 246,508 228,538 147,538" fill="#bba873"/>
    </svg>
    <div class="cover-brand">VELMAR CREST</div>
    <h1 class="cover-heading">YOUR<br><span class="accent">HEADING</span><br>GOES HERE</h1>
    <p class="cover-tagline">We take the risk out of your business so<br>you can focus on what you're good at.</p>
    <div class="cover-doc"><span class="navy">COMPANY</span><br><span class="gold">PROPOSAL<br>2024</span></div>
    <div class="cover-web">VELMARCREST.COM.AU</div>
  </section>

  <!-- Table of contents -->
  <section class="page col-right row-1">
    <svg class="frame" viewBox="0 0 471 666">
      <path d="M0 0 H440 Q432 10 420 10 H0 Z" fill="#bba873"/>
      <path d="M0 642 H471 V666 H0 Z" fill="#13296a"/>
      <path d="M440 642 Q452 636 471 636 V642 Z" fill="#bba873"/>
    </svg>
    <h2 class="page-title"><span class="line-1" style="color:var(--gold)">TABLE OF</span><span class="line-2" style="color:var(--navy)">CONTENTS</span></h2>
    <div class="brand-mini">VELMAR CREST</div>
    <svg class="toc-rail" width="10" height="270" viewBox="0 0 10 270">
      <line x1="2" y1="0" x2="2" y2="266" stroke="#bba873" stroke-width="1" stroke-dasharray="1.5 2"/>
      <circle cx="2" cy="3" r="2.6" fill="#fff" stroke="#bba873" stroke-width=".8"/>
      <circle cx="2" cy="79" r="2.6" fill="#fff" stroke="#bba873" stroke-width=".8"/>
      <circle cx="2" cy="154" r="2.6" fill="#fff" stroke="#bba873" stroke-width=".8"/>
      <circle cx="2" cy="230" r="2.6" fill="#fff" stroke="#bba873" stroke-width=".8"/>
    </svg>
    <div class="toc">
      <div class="toc-group">
        <div class="toc-row toc-row--title"><span class="label">1. TITLE GOES HERE</span><span class="leader"></span><span class="num">1</span></div>
        <div class="toc-row"><span class="label">1.1 Heading Goes Here</span><span class="leader"></span><span class="num">1</span></div>
        <div class="toc-row"><span class="label">1.2 Heading Goes Here</span><span class="leader"></span><span class="num">2</span></div>
      </div>
      <div class="toc-group">
        <div class="toc-row toc-row--title"><span class="label">2. TITLE GOES HERE</span><span class="leader"></span><span class="num">4</span></div>
        <div class="toc-row"><span class="label">1.1 Heading Goes Here</span><span class="leader"></span><span class="num">4</span></div>
        <div class="toc-row"><span class="label">1.2 Heading Goes Here</span><span class="leader"></span><span class="num">5</span></div>
      </div>
      <div class="toc-group">
        <div class="toc-row toc-row--title"><span class="label">3. TITLE GOES HERE</span><span class="leader"></span><span class="num">7</span></div>
        <div class="toc-row"><span class="label">1.1 Heading Goes Here</span><span class="leader"></span><span class="num">7</span></div>
        <div class="toc-row"><span class="label">1.2 Heading Goes Here</span><span class="leader"></span><span class="num">8</span></div>
      </div>
      <div class="toc-group">
        <div class="toc-row toc-row--title"><span class="label">4. TITLE GOES HERE</span><span class="leader"></span><span class="num">10</span></div>
        <div class="toc-row"><span class="label">1.1 Heading Goes Here</span><span class="leader"></span><span class="num">10</span></div>
        <div class="toc-row"><span class="label">1.2 Heading Goes Here</span><span class="leader"></span><span class="num">12</span></div>
      </div>
    </div>
    <div class="footer-text footer-text--left">Information about our Services</div>
    <div class="footer-text footer-text--right">COMPANY PROPOSAL <span class="year">2024</span></div>
  </section>

  <!-- Page: text, quote and table -->
  <section class="page col-left row-2">
    <svg class="frame" viewBox="0 0 471 666">
      <path d="M0 0 H440 Q432 10 420 10 H0 Z" fill="#bba873"/>
      <path d="M0 642 H471 V666 H0 Z" fill="#13296a"/>
      <path d="M85 642 Q95 636 110 636 H471 V642 Z" fill="#bba873"/>
    </svg>
    <h2 class="page-title"><span class="line-1">HEADING</span><span class="line-2">GOES HERE</span></h2>
    <div class="brand-mini">VELMAR CREST</div>
    <div class="content" style="top:107px">
      <h3 class="h-gold">1. TITLE HEADING GOES HERE</h3>
      <p class="body-copy" style="margin-bottom:15px">Lorem ipsum dolor sit amet, consectetuer adipiscing elit, sed diam nonummy nibh euismod tincidunt ut laoreet dolore magna aliquam erat volutpat. Ut wisi enim ad minim veniam, quis nostrud exerci tation ullamcorper suscipit lobortis nisl ut aliquip ex ea tation ullamcorper suscipit lobortis nisl ut aliquip ex ea commodo consequat. Duis autem vel eum iriure dolor in hendrerit in vulputate velit esse molestie consequat, vel illum dolore eu feugiat nulla facilisis at vero eros et accumsan et iusto odio dignis</p>
      <h4 class="h-dark">HEADING 2</h4>
      <p class="body-copy" style="margin-bottom:15px">Lorem ipsum dolor sit amet, consectetuer adipiscing elit, sed diam nonummy nibh euismod tincidunt ut laoreet dolore magna aliquam erat volutpat. Ut wisi enim ad minim veniam, quis nostrud exerci tation ullamcorper suscipit lobortis nisl ut aliquip ex ea tation ullamcorper suscipit lobortis nisl ut aliquip ex ea commodo consequat. Duis autem vel eum iriure dolor in hendrerit in vulputate velit esse molestie consequat, vel illum dolore eu feugiat nulla facilisis at vero eros et accumsan et iusto odio dignis</p>
      <div class="quote">“QUOTE”</div>
      <p class="body-copy" style="margin-bottom:2px">Lorem ipsum dolor sit amet, consectetuer adipiscing elit, sed diam nonummy nibh euismod tincidunt ut laoreet dolore magna aliquam erat volutpat. Ut wisi enim ad minim veniam,</p>
      <p class="body-copy" style="margin-bottom:15px">Lorem ipsum dolor sit amet, consectetuer adipiscing elit, sed diam nonummy nibh euismod tincidunt ut laoreet dolore</p>
      <h4 class="h-dark">HEADING 2</h4>
      <p class="body-copy">Lorem ipsum dolor sit amet, consectetuer adipiscing elit, sed diam nonummy nibh euismod tincidunt ut laoreet dolore magna aliquam erat volutpat. Ut wisi enim ad minim veniam, quis nostrud exerci tation ullamcorper suscipit lobortis nisl ut aliquip ex ea tation ullamcorper suscipit lobortis nisl ut aliquip ex ea commodo consequat. Duis autem vel eum iriure dolor in hendrerit in vulputate velit esse molestie consequat, vel illum dolore eu feugiat nulla facilisis at vero eros et accumsan et iusto odio dignis</p>
    </div>
    <div class="data-table" role="table" aria-label="Sample data table">
      <svg width="424" height="112" viewBox="0 0 424 112" style="position:absolute;left:0;top:-6px">
        <rect x="0" y="6" width="424" height="21" fill="#bba873"/>
        <rect x="130" y="0" width="73" height="110" rx="4" fill="none" stroke="#13296a" stroke-width="1"/>
        <path d="M130 27 V4 Q130 0 134 0 H199 Q203 0 203 4 V27 Z" fill="#13296a"/>
        <g stroke="#cfcfcf" stroke-width=".8">
          <line x1="0" y1="46" x2="424" y2="46"/>
          <line x1="0" y1="65" x2="424" y2="65"/>
          <line x1="0" y1="84" x2="424" y2="84"/>
          <line x1="0" y1="103" x2="424" y2="103"/>
        </g>
      </svg>
      <div class="cell" style="left:3px;top:8px;color:#fff">Heading Goes Here</div>
      <div class="cell head" style="left:130px;top:2px;width:73px">Heading<br>Goes Here</div>
      <div class="cell head" style="left:203px;top:2px;width:73px">Heading<br>Goes Here</div>
      <div class="cell head" style="left:276px;top:2px;width:73px">Heading<br>Goes Here</div>
      <div class="cell head" style="left:349px;top:2px;width:73px">Heading<br>Goes Here</div>

      <div class="cell" style="left:3px;top:30px">Lorem Ipsum Goes Here</div>
      <div class="cell" style="left:163px;top:30px">23</div><div class="cell" style="left:236px;top:30px">12</div><div class="cell" style="left:309px;top:30px">78</div><div class="cell" style="left:382px;top:30px">12</div>
      <div class="cell" style="left:3px;top:49px">Lorem Ipsum Goes Here</div>
      <div class="cell" style="left:163px;top:49px">45</div><div class="cell" style="left:236px;top:49px">56</div><div class="cell" style="left:309px;top:49px">12</div><div class="cell" style="left:382px;top:49px">56</div>
      <div class="cell" style="left:3px;top:68px">Lorem Ipsum Goes Here</div>
      <div class="cell" style="left:163px;top:68px">78</div><div class="cell" style="left:236px;top:68px">76</div><div class="cell" style="left:309px;top:68px">34</div><div class="cell" style="left:382px;top:68px">76</div>
      <div class="cell" style="left:3px;top:87px">Lorem Ipsum Goes Here</div>
      <div class="cell" style="left:163px;top:87px">22</div><div class="cell" style="left:236px;top:87px">12</div><div class="cell" style="left:309px;top:87px">55</div><div class="cell" style="left:382px;top:87px">12</div>
    </div>
    <div class="footer-text footer-text--left">Information about our Services</div>
    <div class="footer-text footer-text--right">COMPANY PROPOSAL <span class="year">2024</span></div>
  </section>

  <!-- Page: text with chart -->
  <section class="page col-right row-2">
    <svg class="frame" viewBox="0 0 471 666">
      <path d="M0 0 H440 Q432 10 420 10 H0 Z" fill="#bba873"/>
      <path d="M0 642 H471 V666 H0 Z" fill="#13296a"/>
      <path d="M440 642 Q452 636 471 636 V642 Z" fill="#bba873"/>
    </svg>
    <h2 class="page-title"><span class="line-1">HEADING</span><span class="line-2">GOES HERE</span></h2>
    <div class="brand-mini">VELMAR CREST</div>
    <div class="content" style="top:107px">
      <h3 class="h-gold">HEADING GOES HERE</h3>
      <p class="body-copy" style="margin-bottom:9px">Lorem ipsum dolor sit amet, consectetuer adipiscing elit, sed diam nonummy nibh euismod tincidunt ut laoreet dolore magna aliquam erat volutpat. Ut wisi enim ad minim veniam, quis nostrud exerci tation ullamcorper suscipit lobortis nisl ut aliquip ex ea tation ullamcorper suscipit lobortis nisl ut aliquip ex ea commodo consequat. Duis autem vel eum iriure dolor in hendrerit in vulputate velit esse molestie consequat, vel illum dolore eu feugiat nulla facilisis at vero eros et accumsan et iusto odio dignis Lorem ipsum dolor sit amet, consectetuer adipiscing elit, sed diam nonummy nibh euismod tincidunt ut laoreet dolore magna aliquam erat volutpat. Ut wisi enim ad minim veniam, quis nostrud exerci tation ullamcorper suscipit lobortis nisl ut aliquip ex ea tation ullamcorper suscipit lobortis nisl ut aliquip ex ea commodo consequat. Duis autem vel eum iriure dolor in hendrerit in vulputate velit esse molestie consequat, vel illum dolore eu feugiat nulla facilisis at vero eros et accumsan et iusto odio dignis</p>
      <h3 class="h-gold">HEADING GOES HERE</h3>
      <p class="body-copy">Lorem ipsum dolor sit amet, consectetuer adipiscing elit, sed diam nonummy nibh euismod tincidunt ut laoreet dolore magna aliquam erat volutpat. Ut wisi enim ad minim veniam, quis nostrud exerci tation ullamcorper suscipit lobortis nisl ut aliquip ex ea tation ullamcorper suscipit lobortis nisl ut aliquip ex ea commodo consequat. Duis autem vel eum iriure dolor in hendrerit in vulputate velit esse molestie consequat, vel illum dolore eu feugiat nulla facilisis at vero eros et accumsan et iusto odio dignis Lorem ipsum dolor sit amet,</p>
    </div>
    <div class="content" style="top:348px;right:auto;width:200px">
      <h4 class="sub-h">1.1. HEADING GOES HERE</h4>
      <div class="list">a) Lorem ipsum dolor sit amet,<br>b)Lorem ipsum dolor sit amet,</div>
      <h4 class="sub-h" style="margin-top:14px">1.2. HEADING GOES HERE</h4>
      <div class="list">a) Lorem ipsum dolor sit amet,<br>b) Lorem ipsum dolor sit amet,<br>c) Lorem ipsum dolor sit amet,<br>d) Lorem ipsum dolor sit amet,</div>
    </div>
    <svg class="chart" width="200" height="120" viewBox="0 0 200 120" role="img" aria-label="Bar chart of temperature in well 20 from 2000 to 2009">
      <text x="18" y="8" font-family="Montserrat, sans-serif" font-size="9.5" font-weight="600" fill="#555">Temperature in well 20 in °C</text>
      <g font-family="Montserrat, sans-serif" font-size="5" fill="#666" text-anchor="end">
        <text x="9" y="27">140</text><text x="9" y="37.5">120</text><text x="9" y="48">100</text>
        <text x="9" y="59">80</text><text x="9" y="69.5">60</text><text x="9" y="80">40</text>
        <text x="9" y="90.5">20</text><text x="9" y="101">0</text>
      </g>
      <g stroke="#e3e3e3" stroke-width=".5">
        <line x1="14" y1="25" x2="190" y2="25"/><line x1="14" y1="35.5" x2="190" y2="35.5"/>
        <line x1="14" y1="46" x2="190" y2="46"/><line x1="14" y1="57" x2="190" y2="57"/>
        <line x1="14" y1="67.5" x2="190" y2="67.5"/><line x1="14" y1="78" x2="190" y2="78"/>
        <line x1="14" y1="88.5" x2="190" y2="88.5"/><line x1="14" y1="99" x2="190" y2="99"/>
      </g>
      <g fill="#bba873">
        <rect x="20" y="69.6" width="12" height="29.4"/>
        <rect x="39.5" y="77" width="12" height="22"/>
        <rect x="59" y="53.9" width="12" height="45.1"/>
        <rect x="78.5" y="51.8" width="12" height="47.2"/>
        <rect x="98" y="47.6" width="12" height="51.4"/>
        <rect x="117.5" y="38.6" width="12" height="60.4"/>
        <rect x="137" y="33.4" width="12" height="65.6"/>
        <rect x="156.5" y="32.3" width="12" height="66.7"/>
        <rect x="176" y="31.3" width="12" height="67.7"/>
      </g>
      <g font-family="Montserrat, sans-serif" font-size="5" fill="#555" text-anchor="middle">
        <text x="26" y="66.5">56</text><text x="45.5" y="74">42</text><text x="65" y="51">86</text>
        <text x="84.5" y="49">90</text><text x="104" y="44.5">98</text><text x="123.5" y="35.5">115</text>
        <text x="143" y="30.5">125</text><text x="162.5" y="29.5">127</text><text x="182" y="28.5">129</text>
        <text x="26" y="108">2000</text><text x="45.5" y="108">2002</text><text x="65" y="108">2003</text>
        <text x="84.5" y="108">2004</text><text x="104" y="108">2005</text><text x="123.5" y="108">2006</text>
        <text x="143" y="108">2007</text><text x="162.5" y="108">2008</text><text x="182" y="108">2009</text>
      </g>
    </svg>
    <div class="footer-text footer-text--left">Information about our Services</div>
    <div class="footer-text footer-text--right">COMPANY PROPOSAL <span class="year">2024</span></div>
  </section>

  <!-- Page: two columns with photo -->
  <section class="page col-left row-3">
    <svg class="frame" viewBox="0 0 471 666">
      <path d="M0 0 H440 Q432 10 420 10 H0 Z" fill="#bba873"/>
      <path d="M0 642 H471 V666 H0 Z" fill="#13296a"/>
      <path d="M85 642 Q95 636 110 636 H471 V642 Z" fill="#bba873"/>
    </svg>
    <h2 class="page-title"><span class="line-1">HEADING</span><span class="line-2">GOES HERE</span></h2>
    <div class="brand-mini">VELMAR CREST</div>
    <div class="col" style="left:27px;top:107px">
      <h3 class="h-section">HEADING GOES HERE</h3>
      <p class="body-copy">Lorem ipsum dolor sit amet, consectetuer adipiscing elit, sed diam nonummy nibh euismod tincidunt ut laoreet dolore magna aliquam erat volutpat. Ut wisi enim ad minim veniam, quis nostrud exerci tation ullamcorper suscipit lobortis nisl ut aliquip ex ea tation ullamcorper suscipit lobortis nisl ut aliquip ex ea commodo consequat. Duis autem vel eum iriure dolor in hendrerit in vulputate velit esse molestie consequat, vel illum dolore eu feugiat nulla facilisis at vero eros et accumsan et iusto odio dignis Lorem ipsum dolor sit amet, consectetuer adipiscing elit, sed diam nonummy nibh euismod tincidunt ut laoreet dolore magna aliquam erat volutpat. Ut wisi enim ad minim veniam, quis nostrud exerci tation ullamcorper suscipit lobortis nisl ut aliquip ex ea tation ullamcorper suscipit lobortis nisl ut aliquip ex ea commodo consequat. Duis autem vel eum iriure dolor in hendrerit in vulputate velit esse molestie consequat, vel illum dolore eu feugiat nulla facilisis at vero eros et accums</p>
      <div class="photo" role="img" aria-label="Photo of two colleagues in a meeting at an office table"></div>
      <p class="body-copy">Lorem ipsum dolor sit amet, consectetuer adipiscing elit, sed diam nonummy nibh euismod tincidunt ut laoreet dolore magna aliquam erat volutpat. Ut wisi enim ad minim veniam, quis nostrud exerci tation tation ullamcorper suscipit lobortis nisl ut aliquip ex ea commodo consequat. Duis autem vel eum iriure dolor in hendrerit in vulputate velit esse molestie</p>
    </div>
    <div class="col" style="left:253px;top:107px">
      <h3 class="h-section">HEADING GOES HERE</h3>
      <p class="body-copy" style="margin-bottom:10px">Lorem ipsum dolor sit amet, consectetuer adipiscing elit, sed diam nonummy nibh euismod tincidunt ut laoreet dolore magna aliquam erat volutpat. Ut wisi enim ad minim veniam, quis nostrud exerci tation ullamcorper suscipit lobortis nisl ut aliquip ex ea tation ullamcorper suscipit lobortis nisl ut aliquip ex ea commodo consequat. Duis autem vel eum iriure dolor in hendrerit in vulputate velit esse molestie consequat, vel illum dolore eu feugiat nulla facilisis at vero eros et accumsan et iusto odio dignis Lorem ipsum dolor sit amet, consectetuer adipiscing elit, sed diam nonummy nibh euismod tincidunt ut laoreet dolore magna aliquam erat volutpat. Ut wisi enim ad minim veniam, quis nostrud exerci tation ullamcorper suscipit lobortis nisl ut aliquip ex ea tation ullamcorper suscipit lobortis nisl ut aliquip ex ea commodo consequat. Duis autem vel eum iriure dolor in hendrerit in vulputate velit esse molestie consequat, vel illum dolore eu feugiat nulla facilisis at vero eros et accums</p>
      <h3 class="h-section">HEADING GOES HERE</h3>
      <p class="body-copy">Lorem ipsum dolor sit amet, consectetuer adipiscing elit, sed diam nonummy nibh euismod tincidunt ut laoreet dolore magna aliquam erat volutpat. Ut wisi enim ad minim veniam, quis nostrud exerci tation ullamcorper suscipit lobortis nisl ut aliquip ex ea tation ullamcorper suscipit lobortis nisl ut aliquip ex ea commodo consequat. Duis autem vel eum iriure dolor in hendrerit in vulputate velit esse molestie consequat, vel illum dolore eu feugiat nulla facilisis at vero eros et accumsan et iusto odio dignis Lorem ipsum dolor sit amet, consectetuer adipiscing elit, sed diam nonummy nibh euismod tincidunt ut laoreet dolore magna aliquam erat volutpat. Ut wisi enim ad minim veniam, quis nostrud exerci tation ullamcorper suscipit lobortis nisl ut aliquip ex ea tation ullamcorper suscipit lobortis nisl ut aliquip ex</p>
    </div>
    <div class="footer-text footer-text--left">Information about our Services</div>
    <div class="footer-text footer-text--right">COMPANY PROPOSAL <span class="year">2024</span></div>
  </section>

  <!-- Page: three sections -->
  <section class="page col-right row-3">
    <svg class="frame" viewBox="0 0 471 666">
      <path d="M0 0 H440 Q432 10 420 10 H0 Z" fill="#bba873"/>
      <path d="M0 642 H471 V666 H0 Z" fill="#13296a"/>
      <path d="M440 642 Q452 636 471 636 V642 Z" fill="#bba873"/>
    </svg>
    <h2 class="page-title"><span class="line-1">HEADING</span><span class="line-2">GOES HERE</span></h2>
    <div class="brand-mini">VELMAR CREST</div>
    <div class="content" style="top:107px">
      <h3 class="h-section">HEADING GOES HERE</h3>
      <p class="body-copy" style="margin-bottom:10px">Lorem ipsum dolor sit amet, consectetuer adipiscing elit, sed diam nonummy nibh euismod tincidunt ut laoreet dolore magna aliquam erat volutpat. Ut wisi enim ad minim veniam, quis nostrud exerci tation ullamcorper suscipit lobortis nisl ut aliquip ex ea tation ullamcorper suscipit lobortis nisl ut aliquip ex ea commodo consequat. Duis autem vel eum iriure dolor in hendrerit in vulputate velit esse molestie consequat, vel illum dolore eu feugiat nulla facilisis at vero eros et accumsan et iusto odio dignis Lorem ipsum dolor sit amet, consectetuer adipiscing elit, sed diam nonummy nibh euismod tincidunt ut laoreet dolore magna aliquam erat volutpat. Ut wisi enim ad minim veniam, quis nostrud exerci tation ullamcorper suscipit lobortis nisl ut aliquip ex ea tation ullamcorper suscipit lobortis nisl ut aliquip ex ea commodo consequat. Duis autem vel eum iriure dolor in hendrerit in vulputate velit esse molestie consequat, vel illum dolore eu feugiat nulla facilisis at vero eros et accumsan et iusto odio dignis</p>
      <h3 class="h-section">HEADING GOES HERE</h3>
      <p class="body-copy" style="margin-bottom:10px">Lorem ipsum dolor sit amet, consectetuer adipiscing elit, sed diam nonummy nibh euismod tincidunt ut laoreet dolore magna aliquam erat volutpat. Ut wisi enim ad minim veniam, quis nostrud exerci tation ullamcorper suscipit lobortis nisl ut aliquip ex ea tation ullamcorper suscipit lobortis nisl ut aliquip ex ea commodo consequat. Duis autem vel eum iriure dolor in hendrerit in vulputate velit esse molestie consequat, vel illum dolore eu feugiat nulla facilisis at vero eros et accumsan et iusto odio dignis Lorem ipsum dolor sit amet,</p>
      <h3 class="h-section">HEADING GOES HERE</h3>
      <p class="body-copy">Lorem ipsum dolor sit amet, consectetuer adipiscing elit, sed diam nonummy nibh euismod tincidunt ut laoreet dolore magna aliquam erat volutpat. Ut wisi enim ad minim veniam, quis nostrud exerci tation ullamcorper suscipit lobortis nisl ut aliquip ex ea tation ullamcorper suscipit lobortis nisl ut aliquip ex ea commodo consequat. Duis autem vel eum iriure dolor in hendrerit in vulputate velit esse molestie consequat, vel illum dolore eu feugiat nulla facilisis at vero eros et accumsan et iusto odio dignis Lorem ipsum dolor sit amet,</p>
    </div>
    <div class="footer-text footer-text--left">Information about our Services</div>
    <div class="footer-text footer-text--right">COMPANY PROPOSAL <span class="year">2024</span></div>
  </section>

</div>
</body>
</html>
```